Electronic hardware design and manufacturer needing a new business card design.

We need a new business card design consisting of a double sided design adhering to brand and logo guidelines attached. I also want to incorporate something that recognizes our 25th year in business ("EST 2001" or something like that....).

Need extra days to review

Need extra days to review

```html
<!DOCTYPE html>
<html lang="en">
<head>
<meta charset="utf-8">
<title>Northvane Circuit Works — Business Card</title>
<link rel="stylesheet" href="https://fonts.googleapis.com/css2?family=Montserrat:wght@400;500;600;700&display=swap">
<style>
  :root {
    --navy: #0b2233;
    --navy-deep: #071c2a;
    --orange: #d9661f;
    --ink: #15293a;
    --steel: #9bb0c8;
    --paper: #f2f2f2;
    --backdrop: #dcdedd;
    --white: #ffffff;
  }
  * { box-sizing: border-box; margin: 0; padding: 0; }
  html, body {
    width: 1200px; height: 1200px; overflow: hidden;
    background: var(--backdrop);
    font-family: "Montserrat", sans-serif;
  }
  .sheet {
    width: 1200px; height: 1200px;
    display: flex; flex-direction: column; align-items: center; justify-content: center;
    gap: 40px;
  }
  .card {
    position: relative;
    width: 900px; height: 514px;
    border-radius: 4px;
    overflow: hidden;
  }
  .card-front { background: var(--paper); color: var(--ink); }
  .card-back { background: var(--navy-deep); }

  .holder { position: absolute; left: 79px; top: 68px; }
  .holder-name {
    font-weight: 700; font-size: 29px; letter-spacing: 1.2px;
    color: var(--orange); text-transform: uppercase; line-height: 1.2;
  }
  .holder-role { font-weight: 400; font-size: 23px; line-height: 1.25; }

  .company { position: absolute; left: 79px; top: 228px; }
  .company-name { font-weight: 600; font-size: 23px; color: var(--orange); line-height: 1.4; }
  .company-address { font-weight: 400; font-size: 23px; line-height: 1.3; }

  .contacts { position: absolute; left: 79px; top: 343px; list-style: none; }
  .contacts li {
    display: flex; align-items: center; gap: 11px;
    font-size: 24px; font-weight: 400; height: 35px; letter-spacing: 0.3px;
  }
  .contacts svg { width: 20px; height: 20px; flex: none; }

  .brand-front {
    position: absolute; left: 575px; top: 120px;
    display: flex; align-items: center; gap: 12px;
  }
  .brand-mark { width: 22px; height: 22px; background: var(--orange); flex: none; }
  .brand-front .brand-name { font-weight: 700; font-size: 40px; color: var(--navy); letter-spacing: -0.5px; }

  .tollfree-band {
    position: absolute; left: 388px; right: 0; bottom: 0; height: 58px;
    background: var(--navy);
    display: flex; align-items: center; justify-content: center;
    color: var(--white); font-size: 23px; font-weight: 400; letter-spacing: 0.3px;
  }

  .brand-back {
    position: absolute; inset: 0;
    display: flex; align-items: center; justify-content: center; gap: 20px;
  }
  .brand-back .brand-mark { width: 36px; height: 36px; }
  .brand-back .brand-name { font-weight: 700; font-size: 72px; color: var(--steel); letter-spacing: -1px; }
</style>
</head>
<body>
<main class="sheet">
  <section class="card card-front" aria-label="Business card front">
    <div class="holder">
      <h1 class="holder-name">Marcus Hale</h1>
      <p class="holder-role">Owner</p>
    </div>

    <div class="brand-front">
      <span class="brand-mark"></span>
      <span class="brand-name">Northvane</span>
    </div>

    <div class="company">
      <p class="company-name">Northvane Circuit Works</p>
      <p class="company-address">1840 Ridgeway Drive SE, Unit 9<br>Redmont, Alberta T4X 1B7</p>
    </div>

    <ul class="contacts">
      <li>
        <svg viewBox="0 0 24 24" aria-hidden="true"><path fill="var(--orange)" d="M6.6 10.8a15.1 15.1 0 0 0 6.6 6.6l2.2-2.2c.3-.3.7-.4 1-.2 1.1.4 2.3.6 3.6.6.6 0 1 .4 1 1V20c0 .6-.4 1-1 1A17 17 0 0 1 3 4c0-.6.4-1 1-1h3.5c.6 0 1 .4 1 1 0 1.3.2 2.5.6 3.6.1.3 0 .7-.2 1z"/></svg>
        (555) 410-2275
      </li>
      <li>
        <svg viewBox="0 0 24 24" aria-hidden="true"><rect x="2" y="5" width="20" height="14" rx="1.5" fill="var(--orange)"/><path d="M3 6.5l9 6.5 9-6.5" stroke="var(--paper)" stroke-width="1.8" fill="none"/></svg>
        hello@northvane.ca
      </li>
      <li>
        <svg viewBox="0 0 24 24" aria-hidden="true"><circle cx="12" cy="12" r="9.5" fill="none" stroke="var(--orange)" stroke-width="2"/><path fill="var(--orange)" d="M7 7.5c2 0 3 1 3 2.5s-1.5 1.5-1.5 3S10 15 10 17l-1.5 1.5C6 17 5 14 5.5 10zM14 5c1 1.5 3 1.5 3 3s-2 1.5-2 3 2 1 3 2.5c-.5 2-2 3.5-3.5 4.5-.5-2 .5-3-1-4s-2-2-1-3.5S14 7.5 13 6z"/></svg>
        www.northvane.ca
      </li>
    </ul>

    <div class="tollfree-band">Toll-free Phone: (855) 410-2275</div>
  </section>

  <section class="card card-back" aria-label="Business card back">
    <div class="brand-back">
      <span class="brand-mark"></span>
      <span class="brand-name">Northvane</span>
    </div>
  </section>
</main>
</body>
</html>
```